Brochure Design Project

I am a Bright Wall Coatings specializing in repainting existing Commercial and Industrial building only in the Auckland N.Z market. I am looking for a tri fold brochure that will be fit into an envelope 130mm x 235mm x 6mm that I can post and also hand to perspective clients when cold calling. Please visit my web site www.brightwallcoatings.co.nz for an overview. I would like the brochure to reflect the web site. Thank you

Reason: To All designers. I am extending the deadline for 7 Days as i have been unable to spend the time to view all design submitted. Thank you all for your effort so far.

Target Market(s)

Property Managers, Building Owners, Building Tenants,

Industry/Entity Type

Building

```html
<!DOCTYPE html>
<html lang="en">
<head>
<meta charset="utf-8">
<title>B.W.C Brochure Panels</title>
<link rel="stylesheet" href="https://fonts.googleapis.com/css2?family=EB+Garamond:ital@1&family=Lexend:wght@600&family=Open+Sans&display=swap">
<style>
  :root {
    --page: #ffffff;
    --navy-deep: #0b3655;
    --navy-mid: #1c5b82;
    --wave-blue: #1f6a93;
    --cream: #dcdfd3;
    --line-grey: #8c98a6;
    --sky-top: #4d82c4;
    --sky-low: #a9c3dc;
    --street: #9c9a92;
    --ink-light: #f2f3f2;
    --tag-ink: #1f3552;
    --tag-ink-light: #e3e8ee;
    --url-ink: #1f3552;
  }
  html, body {
    margin: 0;
    padding: 0;
    width: 1200px;
    height: 1059px;
    overflow: hidden;
    background: var(--page);
  }
  .canvas {
    position: relative;
    width: 1200px;
    height: 1059px;
  }
  .panel {
    position: absolute;
    top: 34px;
    width: 518px;
    height: 989px;
    overflow: hidden;
  }
  .panel--front { left: 52px; }
  .panel--back { left: 626px; }
  .panel svg.panel-art {
    position: absolute;
    inset: 0;
    width: 100%;
    height: 100%;
  }
  .tagline {
    position: absolute;
    left: 0;
    right: 0;
    top: 28px;
    margin: 0;
    text-align: center;
    font-family: "EB Garamond", Georgia, serif;
    font-style: italic;
    font-size: 21px;
    line-height: 25px;
  }
  .panel--front .tagline { color: var(--tag-ink); }
  .panel--back .tagline { color: var(--tag-ink-light); top: 52px; }
  .brand {
    position: absolute;
    left: 0;
    right: 0;
    text-align: center;
    font-family: "Lexend", Arial, sans-serif;
    font-weight: 600;
    color: var(--ink-light);
  }
  .brand__name {
    margin: 0;
    font-size: 78px;
    line-height: 1;
    letter-spacing: 1px;
  }
  .brand__line {
    margin: 14px 0 0;
    font-size: 15px;
    letter-spacing: 4px;
    text-transform: uppercase;
  }
  .panel--front .brand { top: 790px; }
  .panel--back .brand { top: 384px; }
  .web-address {
    position: absolute;
    left: 0;
    right: 0;
    margin: 0;
    text-align: center;
    font-family: "Open Sans", Arial, sans-serif;
    font-size: 14px;
  }
  .panel--front .web-address { top: 928px; color: var(--ink-light); }
  .panel--back .web-address { top: 924px; color: var(--url-ink); }
</style>
</head>
<body>
<div class="canvas">

  <section class="panel panel--front">
    <svg class="panel-art" viewBox="0 0 518 989" preserveAspectRatio="none" aria-hidden="true">
      <defs>
        <radialGradient id="front-glow" cx="0.35" cy="0.72" r="0.7">
          <stop offset="0" stop-color="var(--navy-mid)"/>
          <stop offset="1" stop-color="var(--navy-deep)"/>
        </radialGradient>
        <linearGradient id="photo-tones" x1="0" y1="0" x2="0" y2="1">
          <stop offset="0" stop-color="var(--sky-top)"/>
          <stop offset="0.45" stop-color="var(--sky-low)"/>
          <stop offset="0.75" stop-color="#7e8ea3"/>
          <stop offset="1" stop-color="var(--street)"/>
        </linearGradient>
      </defs>
      <rect class="panel-ground" width="518" height="989" fill="url(#front-glow)"/>
      <path class="wave-cream" d="M0 600 C60 660 130 690 230 690 C340 690 430 650 518 612 V560 H0 Z" fill="var(--cream)"/>
      <path class="wave-line" d="M0 600 C60 660 130 690 230 690 C340 690 430 650 518 612" fill="none" stroke="var(--line-grey)" stroke-width="2"/>
    </svg>
    <svg class="panel-art" viewBox="0 0 518 989" preserveAspectRatio="none" role="img" aria-label="Photograph of a modern multi-storey office building with blue-clad floors on a sunny street corner with a pedestrian crossing">
      <path class="photo-area" d="M0 0 H518 V575 C440 610 350 645 230 650 C120 652 50 610 0 545 Z" fill="url(#photo-tones)"/>
    </svg>
    <p class="tagline">Experience, Expertise and Professional Quality<br>are what you can expect from B.W.C</p>
    <div class="brand">
      <p class="brand__name">B.W.C</p>
      <p class="brand__line">Bright Wall Coatings</p>
    </div>
    <p class="web-address">www.brightwallcoatings.co.nz</p>
  </section>

  <section class="panel panel--back">
    <svg class="panel-art" viewBox="0 0 518 989" preserveAspectRatio="none" aria-hidden="true">
      <defs>
        <radialGradient id="back-glow" cx="0.5" cy="0.42" r="0.65">
          <stop offset="0" stop-color="var(--navy-mid)"/>
          <stop offset="1" stop-color="var(--navy-deep)"/>
        </radialGradient>
      </defs>
      <rect class="panel-ground" width="518" height="989" fill="url(#back-glow)"/>
      <path class="wave-blue" d="M0 690 C20 770 90 800 200 790 C320 778 420 730 518 722 V989 H0 Z" fill="var(--wave-blue)"/>
      <path class="wave-cream" d="M0 700 C20 790 90 825 210 816 C330 806 430 752 518 745 V989 H0 Z" fill="var(--cream)"/>
      <path class="wave-line" d="M140 800 C260 790 380 750 518 750" fill="none" stroke="var(--line-grey)" stroke-width="3"/>
    </svg>
    <p class="tagline">Experience, Expertise and Professional Quality<br>are what you can expect from B.W.C</p>
    <div class="brand">
      <p class="brand__name">B.W.C</p>
      <p class="brand__line">Bright Wall Coatings</p>
    </div>
    <p class="web-address">www.brightwallcoatings.co.nz</p>
  </section>

</div>
</body>
</html>
```